Facebook、Instagram、TwitterなどのSNS広告用のバナー制作をお願いします。
画像内はご自身からのご提供でお願いいたします。
広告使用目的となるため、広告使用可の画像使用をお願いいたします。
※採用となったバナーは当方の著作物とさせていただきますのでご了承ください。

【目的】
弊社は中途の転職支援エージェントです。
弊社のキャリアアドバイザーとキャリア面談に誘導するための
求職者に向けたSNS広告を出すことが目的です。
イメージとして弊社のHP、LPをご確認頂けますと幸いです。
https://www.kuralento.co.jp/
https://www.kuralento.co.jp/lp/

【ターゲット層】
・20代から30代の転職を半年以内に考えている男女
・Web・広告・IT業界に転職したい人

【画像のイメージ】
★作成は2点以上で、下記番号①②=A、③④=B、⑤⑥=Cとして、
A群から1以上、B群から1以上、C群から1以上でご提案ください。
例】
・①と④のイメージ画像で提案→〇
・①と②のイメージ画像で提案→×※両方ともA群のため
・①と②と④のイメージ画像で提案→〇A群とB群のイメージ画像が入っているため

▼画像イメージ▼
①春感を感じるもの

②夏感を感じるもの

③エンジニア経験者の転職支援系

④クリエイティブ(Webデザイナー、Webディレクター・プロデュサーなど)経験者の転職支援系

⑤若手(第二新卒くらい)向け転職支援系

⑥大阪・名古屋・福岡の地方転職支援系

▼下記いずれかの要素を含んだものをお願いします▼
・シンプル/スマート
・爽やか
・やわらかい
・ユニーク
・かわいい
・春感のあるもの
・夏感のあるもの

※画像やイラストは人物ではなく動物でもOKです
【バナー画像に入れていただきたい文言】
・転職
・クラレント、もしくはKuralento

【NG要項】
・他社が出稿しているSNS広告のパクリ
・ごちゃごちゃした印象の画像
・公序良俗に反する文言
・差別的擁護や断定的言葉(絶対に〇〇万円上がる等)
・著作権侵害の可能性がある画像の使用

【希望する色】
エメラルドグリーン系、水色系、パステルカラー系
【納品ファイル】
PNG形式 (.png)

【種類/制作数】
・種類: 静止画(写真、もしくはイラスト)
1点=5,000円
2点=10,000円
ご了承の程よろしくお願い致します。

【ご納品形式】
PNGファイル

以下サイズでご制作ください。
1:1(1,080×1,080)
9:16(1,080×1,920)

色合い、人物、弊社のイメージカラーのエメラルドグリーンがとても綺麗でバランスがよかったです。

デザインを提案していただいた皆様、
どれも素敵なデザインでした。
提案いただき誠にありがとうございます!

```html
<!DOCTYPE html>
<html lang="ja">
<head>
<meta charset="UTF-8">
<title>転職 × 業界経験者 | クラレント</title>
<link rel="stylesheet" href="https://fonts.googleapis.com/css2?family=Noto+Sans+JP:wght@500;700;900&family=Shippori+Mincho:wght@500;700&display=swap">
<style>
  :root {
    --ink: #2b2b2b;
    --bg-top: #f6e9f3;
    --bg-mid: #fbf5fa;
    --bg-bottom: #ffffff;
    --blossom-a: #f5c3d8;
    --blossom-b: #f3dcea;
    --title-a: #1a8fe0;
    --title-b: #18c0f0;
    --band-a: #e8338a;
    --band-b: #b54cd6;
    --accent: #e8338a;
    --marker: #fff23a;
    --skin: #e9d6cc;
    --shirt: #dcd9e0;
    --suit-a: #3f4d80;
    --suit-b: #26315a;
  }
  * { margin: 0; padding: 0; box-sizing: border-box; }
  html, body { width: 675px; height: 1200px; overflow: hidden; }
  body { font-family: "Noto Sans JP", sans-serif; color: var(--ink); }

  .banner {
    position: relative;
    width: 675px;
    height: 1200px;
    overflow: hidden;
    background: linear-gradient(180deg, var(--bg-top) 0%, var(--bg-mid) 35%, var(--bg-bottom) 70%);
  }

  .blossom-photo {
    position: absolute;
    top: 0; right: 0;
    width: 560px; height: 300px;
    background: radial-gradient(ellipse at 70% 15%, var(--blossom-a) 0%, var(--blossom-b) 45%, rgba(255,255,255,0) 75%);
  }

  .portrait-photo {
    position: absolute;
    left: 0; top: 250px;
    width: 480px; height: 950px;
    background: linear-gradient(180deg,
      rgba(233,214,204,0) 0%,
      var(--skin) 14%,
      var(--skin) 34%,
      var(--shirt) 44%,
      var(--suit-a) 58%,
      var(--suit-b) 100%);
    -webkit-mask-image: linear-gradient(90deg, #000 70%, rgba(0,0,0,0) 100%);
    mask-image: linear-gradient(90deg, #000 70%, rgba(0,0,0,0) 100%);
  }

  .headline-main {
    position: absolute;
    left: 45px; top: 52px;
    font-size: 112px;
    font-weight: 900;
    letter-spacing: 4px;
    line-height: 1;
    background: linear-gradient(90deg, var(--title-a), var(--title-b));
    -webkit-background-clip: text;
    background-clip: text;
    color: transparent;
  }
  .headline-cross {
    position: absolute;
    left: 312px; top: 112px;
    font-size: 62px;
    font-weight: 700;
    line-height: 1;
    color: var(--ink);
  }
  .headline-band {
    position: absolute;
    left: 212px; top: 212px;
    width: 463px; height: 66px;
    background: linear-gradient(90deg, var(--band-a), var(--band-b));
    color: #fff;
    font-size: 56px;
    font-weight: 900;
    line-height: 66px;
    padding-left: 18px;
    letter-spacing: 3px;
  }

  .message {
    position: absolute;
    right: 36px; top: 305px;
    height: 380px;
    writing-mode: vertical-rl;
    font-family: "Shippori Mincho", serif;
    font-weight: 700;
    color: var(--ink);
  }
  .message-line {
    display: block;
    font-size: 36px;
    letter-spacing: 2px;
    line-height: 1;
    margin-left: 26px;
  }
  .message-line--brand { font-size: 56px; letter-spacing: 10px; }
  .message-accent { color: var(--accent); font-size: 44px; }

  .job-list {
    position: absolute;
    left: 330px; top: 872px;
    list-style: none;
  }
  .job-list li {
    font-size: 34px;
    font-weight: 500;
    line-height: 1;
    margin-bottom: 45px;
    white-space: nowrap;
  }
  .job-list li span {
    background: linear-gradient(transparent 58%, var(--marker) 58%);
    padding: 0 10px 4px 0;
  }
</style>
</head>
<body>
  <main class="banner">
    <div class="blossom-photo" role="img" aria-label="満開の桜の枝の写真"></div>
    <div class="portrait-photo" role="img" aria-label="腕を組んで微笑むスーツ姿の女性の写真"></div>

    <h1 class="headline-main">転職</h1>
    <span class="headline-cross">×</span>
    <p class="headline-band">業界経験者</p>

    <p class="message">
      <span class="message-line">あなたの<span class="message-accent">経験</span>と理想を</span>
      <span class="message-line message-line--brand">クラレントで</span>
      <span class="message-line">実現しよう。</span>
    </p>

    <ul class="job-list">
      <li><span>・WEBデザイナー</span></li>
      <li><span>・WEBディレクター</span></li>
      <li><span>・ITエンジニア</span></li>
      <li><span>・広告業界</span></li>
    </ul>
  </main>
</body>
</html>
```